Professional and creative business card design for recruiting service providers

Our company supports German medium-sized companies in filling vacancies promptly. For this we use social media marketing and bring our customers into the visibility.

We want a professional but also creative design for our business cards.

Please look at halvenrick-consult.de to get an impression of our CI.

Target Market(s)

Small and medium-sized companies in Germany from the industry

Industry/Entity Type

Industrie, Handwerk

Contact Information for Business Card

Name, Position, Telefonnummer, Email, Website

Colors
EE7325
F08F49
F5BC92
FAE3D3
FDF4ED

Requirements
Must have
• A picture of the employee and in the style of www.halvenrick-consult.de

```html
<!DOCTYPE html>
<html lang="de">
<head>
<meta charset="utf-8">
<title>Halvenrick Consult – Visitenkarte</title>
<link rel="stylesheet" href="https://fonts.googleapis.com/css2?family=Montserrat:wght@700;800&family=Arimo:wght@400;700&display=swap">
<style>
  :root {
    --orange: #ee7325;
    --orange-light: #f08f49;
    --charcoal: #333333;
    --charcoal-deep: #262626;
    --paper: #f7f5f2;
    --white: #ffffff;
    --stage: #e6e4e1;
    --text-dark: #2b2b2b;
  }
  * { box-sizing: border-box; margin: 0; padding: 0; }
  html, body { width: 1200px; height: 856px; overflow: hidden; }
  body {
    background: var(--stage);
    font-family: "Arimo", Arial, sans-serif;
    display: flex;
    align-items: center;
    justify-content: center;
    gap: 48px;
  }
  .card {
    position: relative;
    width: 540px;
    height: 340px;
    background: var(--charcoal);
    overflow: hidden;
    box-shadow: 0 10px 28px rgba(0,0,0,0.25);
  }

  /* Front */
  .portrait {
    position: absolute;
    left: 0; top: 0;
    width: 250px; height: 256px;
    background: linear-gradient(160deg, #4a4a4f 0%, #26262b 55%, #1b1b1f 100%);
  }
  .brand {
    position: absolute;
    display: flex;
    align-items: center;
    gap: 12px;
  }
  .front .brand { left: 280px; top: 44px; }
  .brand-mark {
    width: 30px; height: 30px;
    background: var(--orange);
    flex: none;
  }
  .brand-name {
    font-family: "Montserrat", sans-serif;
    font-weight: 800;
    color: var(--white);
    font-size: 23px;
    line-height: 1.05;
    letter-spacing: 0.5px;
    text-transform: uppercase;
  }
  .person {
    position: absolute;
    left: 280px; top: 128px;
  }
  .person-name {
    font-family: "Montserrat", sans-serif;
    font-weight: 700;
    color: var(--orange);
    font-size: 19px;
    letter-spacing: 0.6px;
    text-transform: uppercase;
  }
  .person-role {
    color: var(--white);
    font-size: 15px;
    margin-top: 4px;
  }
  .contact-band {
    position: absolute;
    left: 0; right: 0; top: 190px;
    height: 96px;
    background: var(--paper);
  }
  .front .portrait { z-index: 2; height: 236px; }
  .contact-list {
    position: absolute;
    right: 22px; top: 12px;
    list-style: none;
    text-align: right;
  }
  .contact-list li {
    display: flex;
    align-items: center;
    justify-content: flex-end;
    gap: 8px;
    color: var(--text-dark);
    font-size: 15px;
    line-height: 24px;
  }
  .contact-list svg { width: 14px; height: 14px; flex: none; }
  .address-band {
    position: absolute;
    left: 0; right: 0; bottom: 0;
    height: 54px;
    background: var(--orange);
    color: var(--white);
    font-size: 14px;
    line-height: 19px;
    text-align: right;
    padding: 8px 22px 0 0;
    z-index: 3;
  }

  /* Back */
  .back-pattern {
    position: absolute;
    inset: 0;
    background:
      radial-gradient(ellipse at 30% 25%, #2d2d2d 0%, transparent 60%),
      linear-gradient(200deg, #2a2a2a 0%, #3a3a3a 55%, #555555 100%);
  }
  .back .brand {
    left: 50%; top: 50%;
    transform: translate(-50%, -50%);
  }
</style>
</head>
<body>

  <section class="card front" aria-label="Vorderseite der Visitenkarte">
    <div class="portrait" role="img" aria-label="Porträtfoto des Mitarbeiters in dunklem Sakko vor dunklem Hintergrund"></div>

    <div class="brand">
      <span class="brand-mark"></span>
      <span class="brand-name">Halvenrick<br>Consult</span>
    </div>

    <div class="person">
      <p class="person-name">Lukas Brenner</p>
      <p class="person-role">Manager</p>
    </div>

    <div class="contact-band">
      <ul class="contact-list">
        <li>0171 394 2207
          <svg viewBox="0 0 24 24" aria-hidden="true"><path fill="var(--orange)" d="M6.6 10.8a15.1 15.1 0 0 0 6.6 6.6l2.2-2.2c.3-.3.7-.4 1-.2 1.1.4 2.3.6 3.6.6.6 0 1 .4 1 1V20c0 .6-.4 1-1 1A17 17 0 0 1 3 4c0-.6.4-1 1-1h3.5c.6 0 1 .4 1 1 0 1.3.2 2.5.6 3.6.1.3 0 .7-.2 1z"/></svg>
        </li>
        <li>info@halvenrick-consult.de
          <svg viewBox="0 0 24 24" aria-hidden="true"><rect x="2.5" y="5" width="19" height="14" fill="none" stroke="var(--orange)" stroke-width="2"/><path d="M3 6l9 7 9-7" fill="none" stroke="var(--orange)" stroke-width="2"/></svg>
        </li>
        <li>www.halvenrick-consult.de
          <svg viewBox="0 0 24 24" aria-hidden="true"><circle cx="12" cy="12" r="9.5" fill="none" stroke="var(--orange)" stroke-width="2"/><path d="M2.5 12h19M12 2.5c3 3 3 16 0 19M12 2.5c-3 3-3 16 0 19" fill="none" stroke="var(--orange)" stroke-width="1.6"/></svg>
        </li>
      </ul>
    </div>

    <address class="address-band" style="font-style:normal">
      Lindenhofer Weg 42b<br>70174 Stuttgart
    </address>
  </section>

  <section class="card back" aria-label="Rückseite der Visitenkarte">
    <div class="back-pattern" role="img" aria-label="Geprägtes Wiederholungsmuster in Dunkelgrau"></div>
    <div class="brand">
      <span class="brand-mark"></span>
      <span class="brand-name">Halvenrick<br>Consult</span>
    </div>
  </section>

</body>
</html>
```